Accounting Practice Business Card Design

I have a logo I am happy for you to use in the design of the Business Card.
You can edit and change colours as you please, I am not fixated on it.
I am looking for a modern and clean overall feel for the finished design.

The business is a small accounting practice who thrives on word of mouth referrals and this card will be given to all current and prospect clients.

Industry/Entity Type

Accountant

Contact Information for Business Card

Marcus Elwin
Level 5, 8 Corvale Ridge Road
ASHGROVE RISE VIC 3187
Phone: 9481 3057
Email: melwin@mrfaccountants.com.au
Web: www.mrfaccountants.com.au

Font styles to use
Serif
Sans Serif

Colors
0555a3
3277b5
85acd3
0393ce
33a6d7
85cae6
00a990
33b8a4
9bcb3c

Requirements
Must have
• "The end to your tax problems begin with us"
• "A referral from you is our greatest compliment"
Nice to have
• Modern clean professional

```html
<!DOCTYPE html>
<html lang="en">
<head>
<meta charset="utf-8">
<title>MRF Accountants – Business Card</title>
<link href="https://fonts.googleapis.com/css2?family=Libre+Baskerville:wght@400;700&family=Open+Sans:wght@700&display=swap" rel="stylesheet">
<style>
  :root {
    --teal: #1aa58e;
    --teal-light: #33b8a4;
    --navy: #0555a3;
    --blue: #1c58b0;
    --white: #ffffff;
    --ink: #1f2a44;
    --page: #ffffff;
  }
  * { margin: 0; padding: 0; box-sizing: border-box; }
  html, body { width: 1200px; height: 900px; overflow: hidden; background: var(--page); }
  .canvas { position: relative; width: 1200px; height: 900px; }

  .card {
    position: absolute;
    left: 300px;
    width: 570px;
    background: var(--teal);
    overflow: hidden;
  }
  .card--front { top: 42px; height: 333px; }
  .card--back  { top: 380px; height: 338px; }
  .card__chevrons { position: absolute; inset: 0; width: 100%; height: 100%; }

  .brand {
    position: absolute; left: 44px; top: 84px;
    display: flex; align-items: center; gap: 8px;
    font-family: "Libre Baskerville", serif; font-weight: 700;
    font-size: 20px; color: var(--navy); letter-spacing: 1px;
  }
  .brand__mark { width: 14px; height: 14px; background: var(--navy); }

  .person { position: absolute; left: 0; width: 330px; text-align: center; }
  .person__name {
    top: 172px;
    font-family: "Libre Baskerville", serif; font-weight: 400;
    font-size: 16px; letter-spacing: 3px; color: var(--navy);
  }
  .person__role {
    top: 203px;
    font-family: "Libre Baskerville", serif;
    font-size: 12px; letter-spacing: 1px; color: var(--ink);
  }
  .tagline {
    position: absolute; left: 2px; top: 280px;
    font-family: "Open Sans", sans-serif; font-weight: 700;
    font-size: 16px; color: var(--white);
  }

  .back__content {
    position: absolute; left: 180px; right: 10px; top: 60px;
    text-align: center; color: var(--white);
    font-family: "Libre Baskerville", serif; font-weight: 700;
  }
  .referral { font-size: 17px; letter-spacing: 2px; line-height: 30px; }
  .address { margin-top: 48px; font-size: 12px; letter-spacing: 2px; line-height: 28px; }
  .online { margin-top: 10px; font-size: 12px; letter-spacing: 1.5px; line-height: 28px; }
</style>
</head>
<body>
<main class="canvas">
  <section class="card card--front">
    <svg class="card__chevrons" viewBox="0 0 570 333" aria-hidden="true">
      <polygon points="570,0 570,333 520,333 520,0" fill="var(--blue)"/>
      <polyline points="590,-20 420,166 590,353" fill="none" stroke="var(--blue)" stroke-width="34"/>
      <polyline points="620,-20 455,166 620,353" fill="none" stroke="var(--white)" stroke-width="26"/>
      <polyline points="660,-20 500,166 660,353" fill="none" stroke="var(--teal-light)" stroke-width="28"/>
      <polyline points="700,-20 540,166 700,353" fill="none" stroke="var(--blue)" stroke-width="30"/>
    </svg>
    <div class="brand"><span class="brand__mark"></span>MRF ACCOUNTANTS</div>
    <p class="person person__name">MARCUS ELWIN</p>
    <p class="person person__role">Accountant</p>
    <p class="tagline">The end to your tax problems begin with us</p>
  </section>

  <section class="card card--back">
    <svg class="card__chevrons" viewBox="0 0 570 338" aria-hidden="true">
      <polyline points="-120,-20 70,169 -120,358" fill="none" stroke="var(--blue)" stroke-width="34"/>
      <polyline points="-150,-20 35,169 -150,358" fill="none" stroke="var(--white)" stroke-width="26"/>
      <polyline points="-190,-20 -5,169 -190,358" fill="none" stroke="var(--blue)" stroke-width="28"/>
    </svg>
    <div class="back__content">
      <p class="referral">A REFERRAL FROM YOU IS<br>OUR GREATEST COMPLIMENT</p>
      <p class="address">Level 5, 8 Corvale Ridge Road<br>ASHGROVE RISE VIC 3187<br>Phone: 9481 3057</p>
      <p class="online">Email: melwin@mrfaccountants.com.au<br>Web: www.mrfaccountants.com.au</p>
    </div>
  </section>
</main>
</body>
</html>
```